配色は 水色・青系・その他 NGは白・ピンク系の色です

縦長 H1400xW600 の置き型看板(SYSTEM記載)
壁 H570xW850 店名ロゴのみ
記載項目
記載内容は
New Club Tovik トヴィク
SYSTEM 1set 50min
20:00~21:00 3.000
21:00~Last 5.000
延長 ハーフ 3.000
1time 5.000
TAX 20%
焼酎・ウイスキー 飲み放題
住所・TEL 〇〇〇
緑系、青系、水色系

店舗代表者が気に入りました

この度は何度も変更等依頼しまして ご対応有難う御座いました

```html
<!DOCTYPE html>
<html lang="ja">
<head>
<meta charset="utf-8">
<title>New Club Tovik — サイン案</title>
<link href="https://fonts.googleapis.com/css2?family=Noto+Sans+JP:wght@500;700&family=Noto+Serif+JP:wght@500;700;900&display=swap" rel="stylesheet">
<style>
  :root {
    --page: #ffffff;
    --label: #222222;
    --blue-light: #2f7fe0;
    --blue-mid: #1a5fc4;
    --blue-deep: #0c3d96;
    --ink: #ffffff;
    --rule: rgba(255,255,255,0.85);
  }
  * { margin: 0; padding: 0; box-sizing: border-box; }
  html, body { width: 739px; height: 1200px; overflow: hidden; background: var(--page); }
  body { position: relative; font-family: "Noto Serif JP", serif; color: var(--ink); }

  .sheet-label {
    position: absolute;
    font-family: "Noto Sans JP", sans-serif;
    font-weight: 500;
    font-size: 20px;
    color: var(--label);
  }

  .sign {
    position: absolute;
    overflow: hidden;
  }
  .sign-texture {
    position: absolute; inset: 0;
    background:
      radial-gradient(ellipse at 25% 20%, rgba(120,190,255,0.45), transparent 55%),
      radial-gradient(ellipse at 80% 70%, rgba(90,160,250,0.35), transparent 50%),
      radial-gradient(ellipse at 60% 35%, rgba(8,40,120,0.35), transparent 45%),
      linear-gradient(160deg, var(--blue-light), var(--blue-mid) 45%, var(--blue-deep));
  }
  .line {
    position: absolute; left: 0; right: 0;
    text-align: center; white-space: nowrap;
    font-weight: 700;
    text-shadow: 0 1px 3px rgba(0,20,80,0.35);
  }
  .rule {
    position: absolute; left: 50%; height: 1px;
    background: var(--rule);
    transform: translateX(-50%);
  }
  .price-row {
    position: absolute; left: 0; right: 0;
    display: flex; justify-content: center; gap: 26px;
    font-weight: 700; white-space: nowrap;
    text-shadow: 0 1px 3px rgba(0,20,80,0.35);
  }
  .price-row span:first-child { min-width: 128px; text-align: left; }
  .price-row span:last-child { min-width: 108px; text-align: right; }
  .pair-row {
    position: absolute; left: 0; right: 0;
    display: flex; justify-content: center; gap: 22px;
    font-weight: 700; white-space: nowrap;
    text-shadow: 0 1px 3px rgba(0,20,80,0.35);
  }

  /* wall sign */
  .wall { left: 148px; top: 62px; width: 455px; height: 270px; }
  .wall .club { top: 60px; font-size: 38px; }
  .wall .name { top: 112px; font-size: 70px; font-weight: 900; }

  /* standing signs */
  .stand { top: 399px; width: 330px; height: 728px; }
  .stand-d1 { left: 39px; }
  .stand-d2 { left: 389px; }
  .stand .club { top: 40px; font-size: 38px; }
  .stand .name { top: 86px; font-size: 62px; font-weight: 900; }
  .stand .kana { top: 176px; font-size: 14px; letter-spacing: 0.9em; padding-left: 0.9em; font-weight: 500; }
  .stand .system { top: 236px; font-size: 24px; }
  .stand .set { top: 270px; font-size: 26px; }
  .stand .ext { font-size: 19px; letter-spacing: 1.2em; padding-left: 1.2em; }
  .stand .drink { font-size: 13px; font-weight: 500; font-family: "Noto Sans JP", sans-serif; }
  .stand .tax { font-size: 12px; font-weight: 500; font-family: "Noto Sans JP", sans-serif; }
  .stand .tel { font-size: 12px; font-weight: 500; font-family: "Noto Sans JP", sans-serif; letter-spacing: 0.05em; }
  .dots { position: absolute; left: 0; right: 0; top: 703px; display: flex; justify-content: center; gap: 3px; }
  .dots i { width: 11px; height: 11px; border: 1px solid var(--ink); border-radius: 50%; }
</style>
</head>
<body>

  <p class="sheet-label" style="left:49px; top:14px;">デザイン修正 B</p>
  <section class="sign wall">
    <div class="sign-texture" role="img" aria-label="青いクシャクシャ紙風のテクスチャ背景"></div>
    <p class="line club">New Club</p>
    <p class="line name">Tovik</p>
  </section>

  <p class="sheet-label" style="left:39px; top:360px;">デザイン修正 D1</p>
  <p class="sheet-label" style="left:389px; top:360px;">デザイン修正 D2</p>

  <section class="sign stand stand-d1">
    <div class="sign-texture" role="img" aria-label="青いクシャクシャ紙風のテクスチャ背景"></div>
    <p class="line club">New Club</p>
    <p class="line name">Tovik</p>
    <p class="line kana">トヴィク</p>
    <p class="line system">SYSTEM</p>
    <p class="line set">1set 50min</p>
    <div class="rule" style="top:316px; width:260px;"></div>
    <div class="price-row" style="top:338px; font-size:18px;"><span>20:00~21:00</span><span>3,000yen</span></div>
    <div class="price-row" style="top:374px; font-size:18px;"><span>21:00~Last</span><span>5,000yen</span></div>
    <div class="rule" style="top:414px; width:260px;"></div>
    <p class="line ext" style="top:432px;">延長</p>
    <div class="price-row" style="top:498px; font-size:18px;"><span>ハーフ</span><span>3,000yen</span></div>
    <div class="price-row" style="top:542px; font-size:18px;"><span>1time</span><span>5,000yen</span></div>
    <div class="rule" style="top:586px; width:260px;"></div>
    <p class="line drink" style="top:604px;">焼酎・ウイスキー　飲み放題</p>
    <div class="rule" style="top:636px; width:120px;"></div>
    <p class="line tax" style="top:652px;">TAX 20%</p>
    <p class="line tel" style="top:676px;">TEL　00-0000-0000</p>
    <div class="dots"><i></i><i></i><i></i><i></i><i></i><i></i><i></i><i></i><i></i><i></i><i></i><i></i><i></i><i></i></div>
  </section>

  <section class="sign stand stand-d2">
    <div class="sign-texture" role="img" aria-label="青いクシャクシャ紙風のテクスチャ背景"></div>
    <p class="line club">New Club</p>
    <p class="line name">Tovik</p>
    <p class="line kana">トヴィク</p>
    <p class="line system">SYSTEM</p>
    <p class="line set">1set 50min</p>
    <div class="rule" style="top:316px; width:260px;"></div>
    <div class="pair-row" style="top:338px; font-size:15px;"><span>20:00~21:00</span><span>21:00~Last</span></div>
    <div class="pair-row" style="top:364px; font-size:20px;"><span>3,000yen</span><span>5,000yen</span></div>
    <div class="rule" style="top:408px; width:260px;"></div>
    <p class="line ext" style="top:426px;">延長</p>
    <div class="pair-row" style="top:476px; font-size:16px; gap:60px;"><span>ハーフ</span><span>1time</span></div>
    <div class="pair-row" style="top:506px; font-size:20px;"><span>3,000yen</span><span>5,000yen</span></div>
    <div class="rule" style="top:556px; width:260px;"></div>
    <p class="line drink" style="top:588px;">焼酎・ウイスキー　飲み放題</p>
    <div class="rule" style="top:622px; width:120px;"></div>
    <p class="line tax" style="top:650px;">TAX 20%</p>
    <p class="line tel" style="top:682px;">TEL　00-0000-0000</p>
  </section>

</body>
</html>
```